Brochure Design Project

PLEASE USE THE ATTACHED WORD DOC ONLY AS A GUIDE- I WANT TO SEE A TRUE DESIGN AND NOT JUST A RECREATE OF MY CONTENT.

We need a brochure that is geared towards a service mentality. less tech/bold and something very approachable.

we will look for a design concept and then finalize the content laters.

Target Market(s)

nurses and business owners

Industry/Entity Type

Tech

```html
<!DOCTYPE html>
<html lang="en">
<head>
<meta charset="utf-8">
<title>Harborview Pharmacy – Trifold Brochure Inside</title>
<link rel="stylesheet" href="https://fonts.googleapis.com/css2?family=Arimo:wght@400;700&display=swap">
<style>
  :root {
    --backdrop: #e4e5e6;
    --paper: #ffffff;
    --brand-blue: #1f6fc1;
    --brand-blue-deep: #1858a3;
    --panel-blue-top: #2a79c6;
    --panel-blue-bottom: #1d5ca8;
    --ink: #2b2b2b;
    --card-grey: #c6c7c9;
    --card-light: #e9eaeb;
    --rule: #4a86c8;
  }
  * { box-sizing: border-box; margin: 0; padding: 0; }
  html, body { width: 1200px; height: 1000px; overflow: hidden; }
  body {
    background: var(--backdrop);
    font-family: "Arimo", Arial, sans-serif;
    position: relative;
  }
  .brochure {
    position: absolute;
    left: 60px; top: 130px;
    width: 1080px; height: 740px;
    display: flex;
    background: var(--paper);
    box-shadow: 0 6px 18px rgba(0,0,0,.12);
  }
  .panel { position: relative; width: 360px; height: 100%; }

  /* Left panel */
  .panel--intro { background: var(--paper); }
  .intro-heading {
    position: absolute; left: 0; top: 22px; width: 345px;
    padding-left: 38px;
    color: var(--brand-blue);
    font-weight: 700; font-size: 23px; line-height: 24px;
  }
  .intro-heading::before {
    content: ""; position: absolute; left: 0; top: 4px;
    width: 24px; height: 136px; background: var(--brand-blue);
  }
  .emblem-art {
    position: absolute; left: 170px; top: 220px;
    width: 190px; height: 500px;
    border-radius: 90px 0 0 90px;
    background: linear-gradient(180deg, #3b8fdc 0%, #1f6fc1 55%, #b9bcc0 100%);
  }
  .service-list {
    position: absolute; left: 22px; top: 420px;
    list-style: none; color: var(--ink);
    font-size: 16px; line-height: 20px;
  }
  .service-list li:first-child::before { content: "•"; margin-right: 6px; }

  /* Middle panel */
  .panel--services {
    background: linear-gradient(180deg, var(--panel-blue-top), var(--panel-blue-bottom));
    color: #fff; padding: 20px 18px 0 22px;
  }
  .lead { font-weight: 700; font-size: 16px; line-height: 20px; }
  .lead h2 { font-size: 16px; }
  .feature { margin-top: 34px; font-size: 15px; line-height: 19px; }
  .feature h3 { font-size: 15px; font-weight: 700; margin-bottom: 2px; }
  .connector { position: absolute; left: 0; top: 0; overflow: visible; pointer-events: none; }

  /* Right panel */
  .panel--benefits { background: #f3f3f3; padding: 10px 8px 0 10px; color: var(--ink); }
  .benefit { font-size: 14.5px; line-height: 19.5px; padding: 6px 10px 8px; }
  .benefit--grey { background: var(--card-grey); border-radius: 14px; }
  .benefit--light { background: var(--card-light); }
  .benefit + .benefit { margin-top: 10px; }
  .brand-mark {
    position: absolute; right: 14px; bottom: 18px;
    display: flex; align-items: center; gap: 6px;
    color: var(--brand-blue-deep); font-size: 17px; font-weight: 400;
  }
  .brand-mark::before { content: ""; width: 14px; height: 14px; background: var(--brand-blue-deep); }
</style>
</head>
<body>
  <section class="brochure">
    <svg class="connector" width="1080" height="740">
      <polyline points="112,166 355,166 355,204 548,204 548,196" fill="none" stroke="var(--rule)" stroke-width="1.2"/>
      <polyline points="488,628 875,628" fill="none" stroke="var(--rule)" stroke-width="1.2"/>
    </svg>

    <div class="panel panel--intro">
      <h1 class="intro-heading">Experts in Customized health care By compounding medications, we can improve patient outcomes and simplify medication administration caregivers</h1>
      <div class="emblem-art" role="img" aria-label="Large blue winged staff with entwined serpents, medical emblem illustration"></div>
      <ul class="service-list">
        <li>Customized</li>
        <li>Preparations</li>
        <li>Liquid Medication</li>
        <li>Suspension</li>
        <li>Dosage form Changes</li>
        <li>Transdermal Pain</li>
        <li>Management for site</li>
        <li>Specific therapy</li>
        <li>Dye-Free therapy for</li>
        <li>Allergic patients</li>
        <li>Slow Release Capsules</li>
        <li>Customized dosage for kidney or</li>
        <li>liver failure patients</li>
      </ul>
    </div>

    <div class="panel panel--services">
      <div class="lead">
        <h2>Service:</h2>
        <p>&nbsp;Our service sets us apart from retail pharmacies as well as large impersonal pharmacies. As your pharmacy partner, you'll have access to our pharmacy owners knowledge staff to address concerns, find solutions, and ultimately provide better care while increasing your profitability.</p>
      </div>
      <div class="feature" style="margin-top:40px">
        <h3>Timely Deliveries</h3>
        <p>When it comes to timely deliveries, Harborview has multiple solutions to get you the medications you need quickly. With our pharmacy network, we can deliver medications at anytime, for any reason.</p>
      </div>
      <div class="feature">
        <h3>MAR or EMAR</h3>
        <p>We support EMAR or provide paper MARs if desired. Our goal is to work with your current system, not against it.</p>
      </div>
      <div class="feature">
        <h3>Customized Formularies</h3>
        <p>We help you manage healthcare costs and limit staff dispensing time by creating formularies that focus on generic and customized compounded medications.</p>
      </div>
    </div>

    <div class="panel panel--benefits">
      <div class="benefit benefit--grey">
        <p>•Technology Solutions</p>
        <p>•Harborview provides great time saving technology solutions that you won't find with other local retail pharmacies. We are constantly offer new and exciting ways to reduce staff time and increase profitability</p>
      </div>
      <div class="benefit benefit--light">
        <p>•Medicare Part D Partners</p>
        <p>•We handle therapeutic interchange, prior authorizations, and physician global authorizations so you don't have to.</p>
      </div>
      <div class="benefit benefit--grey">
        <p>Medicare Part A</p>
        <p>Utilizing our pharmacy network, we minimize billing issues with price transparency and accuracy. This allows us focus on corporate strategies to manage your pharmacy expenses. Monthly reports helps identify trends, non-formulary utilization and clinical standards so your facility is saving time and money.</p>
      </div>
      <div class="benefit benefit--light">
        <p>Consultant Pharmacists</p>
        <p>Our pharmacists provide regular compliance assistance to minimize your risk and reduce issues during facility surveys.</p>
      </div>
      <div class="benefit benefit--grey">
        <p>Continuing Education</p>
        <p>CE for caretakers leads to better outcomes for your residents and your bottom line.</p>
      </div>
      <div class="brand-mark">Harborview</div>
    </div>
  </section>
</body>
</html>
```